Now Leasing Banner

Looking for a banner that says the following information approx 4' x 30'

Now Leasing Maple Ridge Court 925-318-6042

Target Market(s)

Drive by traffic

Industry/Entity Type

Residential property management

Requirements
Must have
• Clear and readable from a distance

```html
<!DOCTYPE html>
<html lang="en">
<head>
<meta charset="utf-8">
<title>Now Leasing Banner – Maple Ridge Court</title>
<link rel="stylesheet" href="https://fonts.googleapis.com/css2?family=Bebas+Neue&family=Pinyon+Script&display=swap">
<style>
  :root {
    --page: #ffffff;
    --banner: #9fab80;
    --banner-edge: #b9bfae;
    --banner-light: #aab68c;
    --brown: #4a2e10;
    --forest: #32564a;
    --white: #ffffff;
    --pale-lime: #d8eca2;
    --text-glow: rgba(255, 255, 255, 0.55);
  }
  html, body {
    margin: 0;
    width: 1200px;
    height: 325px;
    overflow: hidden;
    background: var(--page);
  }
  .canvas {
    position: relative;
    width: 1200px;
    height: 325px;
  }
  .banner {
    position: absolute;
    left: 41px;
    top: 87px;
    width: 1135px;
    height: 151px;
    background: var(--banner);
    border: 1px solid var(--banner-edge);
    box-shadow: 0 2px 4px rgba(0, 0, 0, 0.18);
    overflow: hidden;
  }
  .banner-texture {
    position: absolute;
    inset: 0;
    background:
      linear-gradient(90deg, var(--banner-light) 0%, transparent 30%, transparent 68%, var(--banner-light) 100%);
  }
  .headline {
    position: absolute;
    left: 47px;
    top: 17px;
    margin: 0;
    font-family: "Bebas Neue", "Oswald", sans-serif;
    font-weight: 400;
    font-size: 134px;
    line-height: 1;
    letter-spacing: 1px;
    white-space: nowrap;
    text-shadow: 0 0 2px var(--text-glow);
  }
  .headline-now { color: var(--brown); }
  .headline-leasing { color: var(--forest); }
  .contact {
    position: absolute;
    left: 615px;
    width: 470px;
    top: 0;
    height: 151px;
    text-align: center;
  }
  .property-name {
    margin: 0;
    padding-top: 6px;
    font-family: "Pinyon Script", cursive;
    font-size: 50px;
    line-height: 1.05;
    color: var(--white);
    white-space: nowrap;
  }
  .phone {
    display: block;
    margin-top: -2px;
    font-family: "Bebas Neue", "Oswald", sans-serif;
    font-size: 90px;
    line-height: 1;
    color: var(--forest);
    -webkit-text-stroke: 6px var(--pale-lime);
    paint-order: stroke fill;
    white-space: nowrap;
    text-decoration: none;
  }
</style>
</head>
<body>
  <div class="canvas">
    <section class="banner" aria-label="Now Leasing banner">
      <div class="banner-texture" role="img" aria-label="Subtle diagonal line texture in light sage green"></div>
      <h1 class="headline"><span class="headline-now">NOW</span> <span class="headline-leasing">LEASING</span></h1>
      <div class="contact">
        <p class="property-name">Maple Ridge Court</p>
        <a class="phone" href="tel:9253186042">925-318-6042</a>
      </div>
    </section>
  </div>
</body>
</html>
```